Powerpoint Template for a cool IT Recruiting and Consulting Company

We need to have a PowerPoint template designed for our company. We are a Technology Consulting and Recruiting company in Canada.

I'm not looking for an explosion of colours, stay elegant and sharp.

The message that it needs to portray a cool tech company utilizing the blue in our logo but also professionalism and an excitement feel about it that makes clients want to do business with us.

I have attached 2 screenshots of the logo options and also the PDF of them.

Looking forward to seeing the results.

Target Market(s)

We sell our services to Banks, Government and other Tech Companies

Industry/Entity Type

It Service

Font styles to use
Sans Serif

Colors
0592cd

Requirements
Must have
• Logo
Nice to have
Should not have
• Lots of colours

```html
<!DOCTYPE html>
<html lang="en">
<head>
<meta charset="utf-8">
<title>Nexora Presentation Template</title>
<link rel="stylesheet" href="https://fonts.googleapis.com/css2?family=Raleway:wght@400;500;600;700;800&display=swap">
<style>
:root{
  --blue:#4c78a8;
  --blue-deep:#3b6592;
  --blue-soft:#7d9fc4;
  --blue-mid:#6187b3;
  --ink:#1a1a1a;
  --text:#3c3c3c;
  --muted:#8a8a8a;
  --gray:#6f6f6f;
  --gray-soft:#a7a3a0;
  --line:#dedede;
  --paper:#ffffff;
  --canvas:#f3f3f3;
}
*{box-sizing:border-box;margin:0;padding:0}
html,body{width:1200px;height:2291px;overflow:hidden;background:var(--canvas)}
body{font-family:"Raleway",Arial,sans-serif;color:var(--text)}
.deck{width:1200px;height:2291px;display:grid;grid-template-columns:repeat(3,396px);grid-auto-rows:223px;gap:6px;padding-top:3px;overflow:hidden}
.slide{position:relative;overflow:hidden;background:var(--paper);box-shadow:0 0 0 1px #e4e4e4}
.abs{position:absolute}
.photo{position:absolute}
.tiny{font-size:4.6px;line-height:1.45;color:var(--muted)}
.tiny.light{color:rgba(255,255,255,.85)}
.s-title{position:absolute;left:14px;top:11px;font-size:11px;font-weight:700;color:#333}
.brand{display:inline-flex;align-items:center;gap:3px;font-weight:700;color:var(--blue);letter-spacing:-.2px}
.brand .dot{border-radius:50%;border:2px solid currentColor}
.brand.white{color:#fff}
.foot{position:absolute;left:0;right:0;bottom:0;height:19px;border-top:1px solid var(--line);background:#fff;display:flex;align-items:center;justify-content:space-between;padding:0 11px}
.foot .brand{font-size:9px}
.foot .brand .dot{width:7px;height:7px;border-width:1.5px}
.foot .copy{font-size:4.3px;color:#999}
.foot .num{width:9px;height:9px;border-radius:50%;border:1px solid var(--blue);font-size:4px;color:var(--blue);display:flex;align-items:center;justify-content:center}
.h-big{font-weight:700;color:#fff;line-height:1.1}
.sub{font-size:5.5px;color:#fff;opacity:.9}
.ico{border-radius:50%;display:flex;align-items:center;justify-content:center}
.ico svg{display:block}
.cell-text{font-size:4.5px;line-height:1.45;color:rgba(255,255,255,.9)}

/* photo placeholders: soft gradients in each photo's main tones */
.ph-desk-blue{background:
  radial-gradient(ellipse 60% 45% at 78% 72%,rgba(24,42,70,.55),transparent 70%),
  radial-gradient(ellipse 50% 40% at 22% 25%,rgba(170,195,225,.55),transparent 70%),
  radial-gradient(ellipse 40% 30% at 55% 45%,rgba(110,145,185,.6),transparent 70%),
  linear-gradient(120deg,#5a84b2,#41699a 60%,#6a8fba)}
.ph-handshake{background:
  radial-gradient(ellipse 22% 55% at 30% 62%,rgba(28,45,72,.6),transparent 75%),
  radial-gradient(ellipse 22% 55% at 68% 60%,rgba(28,45,72,.55),transparent 75%),
  radial-gradient(ellipse 60% 40% at 50% 10%,rgba(185,205,230,.55),transparent 75%),
  linear-gradient(100deg,#4a72a0,#5f87b3 50%,#43699a)}
.ph-typing{background:
  radial-gradient(ellipse 45% 40% at 60% 60%,rgba(150,150,150,.55),transparent 70%),
  radial-gradient(ellipse 35% 30% at 25% 30%,rgba(90,90,90,.7),transparent 70%),
  linear-gradient(135deg,#1e1e1e,#3b3b3b 60%,#545454)}
.ph-meeting{background:
  radial-gradient(ellipse 40% 35% at 30% 25%,rgba(240,235,225,.8),transparent 70%),
  radial-gradient(ellipse 55% 40% at 55% 75%,rgba(95,70,55,.6),transparent 70%),
  radial-gradient(ellipse 25% 30% at 80% 40%,rgba(200,90,70,.35),transparent 70%),
  linear-gradient(135deg,#9c8772,#cdbba5 50%,#7d6857)}
.ph-tablet{background:
  radial-gradient(ellipse 40% 45% at 55% 55%,rgba(70,80,92,.55),transparent 70%),
  radial-gradient(ellipse 50% 40% at 20% 20%,rgba(250,250,250,.8),transparent 70%),
  linear-gradient(135deg,#c9ccd0,#a4a9ae 60%,#dadcde)}
.ph-plane{background:
  radial-gradient(ellipse 45% 40% at 40% 60%,rgba(60,60,60,.55),transparent 70%),
  radial-gradient(circle at 80% 30%,rgba(200,40,40,.55),transparent 14%),
  linear-gradient(135deg,#eeeeee,#bdbdbd 60%,#8f8f8f)}
.ph-office-a{background:
  radial-gradient(ellipse 50% 45% at 35% 60%,rgba(60,75,90,.5),transparent 70%),
  radial-gradient(ellipse 40% 35% at 80% 20%,rgba(235,240,245,.8),transparent 70%),
  linear-gradient(135deg,#9aa7b3,#cfd7df)}
.ph-office-b{background:
  radial-gradient(ellipse 45% 45% at 50% 55%,rgba(40,45,55,.5),transparent 70%),
  linear-gradient(135deg,#8a939d,#d3d8dd)}
.ph-office-c{background:
  radial-gradient(ellipse 50% 40% at 40% 65%,rgba(110,85,65,.5),transparent 70%),
  radial-gradient(ellipse 40% 35% at 75% 25%,rgba(245,240,230,.8),transparent 70%),
  linear-gradient(135deg,#a39482,#d9cbb8)}
.ph-about{background:
  radial-gradient(ellipse 40% 35% at 55% 45%,rgba(210,180,150,.65),transparent 70%),
  radial-gradient(ellipse 45% 40% at 25% 80%,rgba(30,20,15,.7),transparent 70%),
  radial-gradient(ellipse 30% 25% at 80% 15%,rgba(240,200,150,.5),transparent 70%),
  linear-gradient(135deg,#3a2a22,#7a5b45 55%,#b69478)}
.ph-suit{background:
  radial-gradient(ellipse 28% 60% at 55% 45%,rgba(25,45,75,.55),transparent 75%),
  radial-gradient(ellipse 50% 40% at 15% 15%,rgba(170,195,225,.45),transparent 70%),
  linear-gradient(110deg,#6a8cb3,#4c78a8 55%,#3a6290)}
.ph-towers{background:
  radial-gradient(ellipse 15% 45% at 55% 70%,rgba(30,35,45,.55),transparent 75%),
  repeating-linear-gradient(90deg,rgba(255,255,255,0) 0 18px,rgba(120,140,160,.18) 18px 20px),
  linear-gradient(180deg,#dfe7ef,#a9b8c7 60%,#7d8b99)}
.ph-brand{background:
  radial-gradient(ellipse 40% 35% at 55% 45%,rgba(150,110,95,.45),transparent 70%),
  radial-gradient(ellipse 50% 40% at 30% 80%,rgba(40,40,45,.55),transparent 70%),
  linear-gradient(135deg,#8a8f95,#d2d5d8 60%,#a7abb0)}
.ph-city{background:
  radial-gradient(ellipse 70% 45% at 50% 30%,rgba(180,190,200,.45),transparent 75%),
  repeating-linear-gradient(90deg,rgba(255,255,255,0) 0 22px,rgba(170,180,190,.15) 22px 30px),
  linear-gradient(180deg,#e3e7eb,#f3f4f5 70%,#ffffff)}
.ph-building{background:
  radial-gradient(ellipse 35% 60% at 45% 70%,rgba(25,45,75,.45),transparent 75%),
  repeating-linear-gradient(90deg,rgba(255,255,255,0) 0 26px,rgba(255,255,255,.06) 26px 28px),
  linear-gradient(135deg,#5a82ae,#3f6894 60%,#5f86b1)}
.ph-service{background:
  radial-gradient(ellipse 35% 45% at 60% 55%,rgba(30,45,70,.5),transparent 72%),
  radial-gradient(ellipse 45% 40% at 20% 20%,rgba(250,250,252,.85),transparent 70%),
  linear-gradient(135deg,#dfe4ea,#9aa6b3)}
.ph-map{background:radial-gradient(ellipse 50% 48% at 50% 50%,#c6c6c6,#d6d6d6 55%,rgba(255,255,255,0) 78%)}
</style>
</head>
<body>
<main class="deck">

<section class="slide">
  <div class="abs brand" style="left:70px;top:78px;font-size:60px;gap:10px"><span class="dot" style="width:46px;height:46px;border-width:6px"></span>Nexora</div>
</section>

<section class="slide" style="background:var(--blue)">
  <div class="photo ph-desk-blue" role="img" aria-label="Blue toned photo of a laptop on an office desk" style="inset:0"></div>
  <div class="abs brand white" style="left:32px;top:42px;font-size:17px"><span class="dot" style="width:12px;height:12px"></span>Nexora</div>
  <div class="abs h-big" style="left:32px;top:70px;font-size:20px">Your Title Goes Here</div>
  <div class="abs sub" style="left:32px;top:96px">Your Subtitle Goes Here</div>
  <svg class="abs" style="left:0;bottom:0" width="396" height="50" viewBox="0 0 396 50"><path d="M0 38 Q150 10 396 14 L396 50 L0 50Z" fill="#fff"/><path d="M0 38 Q150 10 396 14" stroke="#1c1c1c" stroke-width="3" fill="none"/></svg>
  <div class="abs tiny" style="right:40px;bottom:10px;color:var(--blue)">www.nexora.example</div>
</section>

<section class="slide">
  <div class="abs" style="left:0;top:0;width:396px;height:140px;background:var(--blue)"></div>
  <div class="abs" style="left:300px;top:150px;background:var(--ink);color:#fff;font-size:6px;padding:2px 12px">Jane Doe</div>
  <div class="abs" style="left:18px;top:166px;font-size:20px;font-weight:700;color:var(--ink)">Your Title Goes Here</div>
  <div class="abs" style="left:18px;top:190px;font-size:6px;color:#555">Your Subtitle Goes Here</div>
  <div class="abs brand" style="right:18px;top:190px;font-size:13px"><span class="dot" style="width:9px;height:9px"></span>Nexora</div>
</section>

<section class="slide">
  <div class="abs brand" style="left:26px;top:80px;font-size:11px"><span class="dot" style="width:8px;height:8px"></span>Nexora</div>
  <div class="abs" style="left:26px;top:100px;font-size:21px;font-weight:700;color:var(--blue)">Your Title Here</div>
  <div class="abs" style="left:26px;top:126px;font-size:6px;color:#555">Your Subtitle Goes Here</div>
</section>

<section class="slide">
  <div class="photo ph-handshake" role="img" aria-label="Blue toned photo of two business people shaking hands" style="inset:0"></div>
  <div class="abs brand white" style="left:0;right:0;top:58px;justify-content:center;font-size:19px"><span class="dot" style="width:13px;height:13px"></span>Nexora</div>
  <div class="abs h-big" style="left:0;right:0;top:88px;text-align:center;font-size:19px">Your Title Goes Here</div>
  <div class="abs sub" style="left:0;right:0;top:112px;text-align:center">Your Subtitle Goes Here</div>
</section>

<section class="slide">
  <div class="s-title" style="color:var(--blue)">Our Agenda</div>
  <div class="abs" style="left:58px;top:38px;width:130px">
    <div style="display:flex;gap:8px;margin-bottom:17px"><svg width="9" height="12"><circle cx="4.5" cy="3" r="2.5" fill="#4c78a8"/><rect x="1" y="6" width="7" height="6" rx="2" fill="#4c78a8"/></svg><div><div style="font-size:6.5px;color:var(--blue)">Agenda One</div><div class="tiny">Brief line about the first topic<br>and what we will cover today.</div></div></div>
    <div style="display:flex;gap:8px;margin-bottom:17px"><svg width="9" height="12"><circle cx="4.5" cy="3" r="2.5" fill="#4c78a8"/><rect x="1" y="6" width="7" height="6" rx="2" fill="#4c78a8"/></svg><div><div style="font-size:6.5px;color:var(--blue)">Agenda Two</div><div class="tiny">Brief line about the second topic<br>and what we will cover today.</div></div></div>
    <div style="display:flex;gap:8px"><svg width="9" height="12"><circle cx="4.5" cy="3" r="2.5" fill="#4c78a8"/><rect x="1" y="6" width="7" height="6" rx="2" fill="#4c78a8"/></svg><div><div style="font-size:6.5px;color:var(--blue)">Agenda Three</div><div class="tiny">Brief line about the third topic<br>and what we will cover today.</div></div></div>
  </div>
  <div class="abs" style="left:215px;top:38px;width:140px">
    <div style="display:flex;gap:8px;margin-bottom:17px"><svg width="9" height="12"><circle cx="4.5" cy="3" r="2.5" fill="#4c78a8"/><rect x="1" y="6" width="7" height="6" rx="2" fill="#4c78a8"/></svg><div><div style="font-size:6.5px;color:var(--blue)">Agenda Four</div><div class="tiny">Brief line about the fourth topic<br>and what we will cover today.</div></div></div>
    <div style="display:flex;gap:8px;margin-bottom:17px"><svg width="9" height="12"><circle cx="4.5" cy="3" r="2.5" fill="#4c78a8"/><rect x="1" y="6" width="7" height="6" rx="2" fill="#4c78a8"/></svg><div><div style="font-size:6.5px;color:var(--blue)">Agenda Five</div><div class="tiny">Brief line about the fifth topic<br>and what we will cover today.</div></div></div>
    <div style="display:flex;gap:8px"><svg width="9" height="12"><circle cx="4.5" cy="3" r="2.5" fill="#4c78a8"/><rect x="1" y="6" width="7" height="6" rx="2" fill="#4c78a8"/></svg><div><div style="font-size:6.5px;color:var(--blue)">Agenda Six</div><div class="tiny">Brief line about the sixth topic<br>and what we will cover today.</div></div></div>
  </div>
  <div class="foot"><span class="brand"><span class="dot"></span>Nexora</span><span class="copy">© Copyright Nexora. All rights reserved</span><span class="num">6</span></div>
</section>

<section class="slide">
  <div class="s-title">Bullets Point 1 Level</div>
  <div class="abs" style="left:24px;top:60px;width:110px"><div style="font-size:6px;color:var(--blue)">● &nbsp;Your Text Here</div><div class="tiny" style="padding-left:10px">Short note on this point<br>with a little more detail.</div></div>
  <div class="abs" style="left:152px;top:60px;width:110px"><div style="font-size:6px;color:var(--ink);font-weight:600">● &nbsp;Your Text Here</div><div class="tiny" style="padding-left:10px">Short note on this point<br>with a little more detail.</div></div>
  <div class="abs" style="left:278px;top:60px;width:110px"><div style="font-size:6px;color:var(--gray)">● &nbsp;Your Text Here</div><div class="tiny" style="padding-left:10px">Short note on this point<br>with a little more detail.</div></div>
  <div class="abs" style="left:24px;top:128px;width:110px"><div style="font-size:6px;color:var(--blue)">● &nbsp;Your Text Here</div><div class="tiny" style="padding-left:10px">Short note on this point<br>with a little more detail.</div></div>
  <div class="abs" style="left:152px;top:128px;width:110px"><div style="font-size:6px;color:var(--ink);font-weight:600">● &nbsp;Your Text Here</div><div class="tiny" style="padding-left:10px">Short note on this point<br>with a little more detail.</div></div>
  <div class="abs" style="left:278px;top:128px;width:110px"><div style="font-size:6px;color:var(--gray)">● &nbsp;Your Text Here</div><div class="tiny" style="padding-left:10px">Short note on this point<br>with a little more detail.</div></div>
  <div class="foot"><span class="brand"><span class="dot"></span>Nexora</span><span class="copy">© Copyright Nexora. All rights reserved</span><span class="num">7</span></div>
</section>

<section class="slide">
  <div class="s-title">Four Elements to consider</div>
  <div class="abs" style="left:30px;top:55px;width:44px;height:44px;border:1.5px solid var(--blue);display:flex;align-items:center;justify-content:center"><svg width="16" height="18"><path d="M3 2V17M3 3H13L11 7L13 11H3" stroke="#4c78a8" fill="none" stroke-width="1.2"/></svg></div>
  <div class="abs" style="left:117px;top:55px;width:44px;height:44px;border:3px solid var(--ink);display:flex;align-items:center;justify-content:center"><svg width="18" height="16"><path d="M1 1H17V11H7L3 15V11H1Z" stroke="#1a1a1a" fill="none" stroke-width="1.2"/><path d="M4 5H14M4 8H11" stroke="#1a1a1a"/></svg></div>
  <div class="abs" style="left:204px;top:55px;width:44px;height:44px;border:1.5px solid var(--gray);display:flex;align-items:center;justify-content:center"><svg width="14" height="18"><circle cx="7" cy="7" r="5.5" stroke="#6f6f6f" fill="none" stroke-width="1.2"/><path d="M5 13H9M5 15.5H9" stroke="#6f6f6f" stroke-width="1.2"/></svg></div>
  <div class="abs" style="left:291px;top:55px;width:44px;height:44px;border:1.5px solid var(--gray-soft);display:flex;align-items:center;justify-content:center"><svg width="18" height="18"><circle cx="9" cy="9" r="7" stroke="#a7a3a0" fill="none" stroke-width="1.2"/><circle cx="9" cy="9" r="2.5" stroke="#a7a3a0" fill="none"/></svg></div>
  <div class="abs" style="left:18px;top:128px;width:68px;text-align:center"><div style="font-size:5px;letter-spacing:.6px;font-weight:700;color:#333">TITLE ONE</div><div class="tiny">A short line about<br>the first element.</div></div>
  <div class="abs" style="left:105px;top:128px;width:68px;text-align:center"><div style="font-size:5px;letter-spacing:.6px;font-weight:700;color:#333">TITLE TWO</div><div class="tiny">A short line about<br>the second element.</div></div>
  <div class="abs" style="left:192px;top:128px;width:68px;text-align:center"><div style="font-size:5px;letter-spacing:.6px;font-weight:700;color:#333">TITLE THREE</div><div class="tiny">A short line about<br>the third element.</div></div>
  <div class="abs" style="left:279px;top:128px;width:68px;text-align:center"><div style="font-size:5px;letter-spacing:.6px;font-weight:700;color:#333">TITLE FOUR</div><div class="tiny">A short line about<br>the fourth element.</div></div>
  <div class="foot"><span class="brand"><span class="dot"></span>Nexora</span><span class="copy">© Copyright Nexora. All rights reserved</span><span class="num">8</span></div>
</section>

<section class="slide">
  <div class="abs" style="left:0;top:0;width:198px;height:80px;background:var(--blue);padding:8px 10px"><div class="cell-text" style="font-size:5.5px">Our team connects skilled technology talent with the banks, public agencies and tech firms that need them most, quickly and with care at every step.</div></div>
  <div class="photo ph-typing" role="img" aria-label="Photo of hands typing on a laptop" style="left:198px;top:0;width:198px;height:80px"></div>
  <div class="photo ph-meeting" role="img" aria-label="Photo of a team meeting around a table" style="left:0;top:80px;width:198px;height:68px"></div>
  <div class="abs" style="left:198px;top:80px;width:198px;height:68px;background:#5d5d5d;padding:8px 10px"><div class="cell-text" style="font-size:5.5px">We review every role in depth, then match people on skill, culture and long term growth for both sides.</div></div>
  <div class="abs" style="left:0;top:148px;width:198px;height:75px;background:var(--gray-soft);padding:8px 10px"><div class="cell-text" style="font-size:5.5px">From first call to final offer, one partner guides the whole hiring process for you.</div></div>
  <div class="photo ph-tablet" role="img" aria-label="Photo of a hand holding a tablet" style="left:198px;top:148px;width:198px;height:75px"></div>
</section>

<section class="slide">
  <div class="s-title">Your Title Here</div>
  <div class="abs" style="left:0;top:62px;width:396px;height:100px;display:grid;grid-template-columns:repeat(4,1fr)">
    <div style="background:var(--blue);padding:10px 8px;text-align:center"><svg width="14" height="14"><circle cx="7" cy="7" r="6" stroke="#fff" fill="none"/><path d="M4 7H10M7 4V10" stroke="#fff"/></svg><div style="font-size:6px;color:#fff;margin:5px 0 3px">Heading Here</div><div class="cell-text" style="text-align:left">Short note on this topic with a few words of detail for the team.</div></div>
    <div style="background:var(--ink);padding:10px 8px;text-align:center"><svg width="14" height="14"><circle cx="7" cy="6" r="4" stroke="#fff" fill="none"/><path d="M7 10V13" stroke="#fff"/></svg><div style="font-size:6px;color:#fff;margin:5px 0 3px">Heading Here</div><div class="cell-text" style="text-align:left">Short note on this topic with a few words of detail for the team.</div></div>
    <div style="background:var(--gray);padding:10px 8px;text-align:center"><svg width="14" height="14"><rect x="2" y="3" width="10" height="8" stroke="#fff" fill="none"/></svg><div style="font-size:6px;color:#fff;margin:5px 0 3px">Heading Here</div><div class="cell-text" style="text-align:left">Short note on this topic with a few words of detail for the team.</div></div>
    <div style="background:var(--gray-soft);padding:10px 8px;text-align:center"><svg width="14" height="14"><circle cx="7" cy="7" r="5" stroke="#fff" fill="none"/><circle cx="7" cy="7" r="1.5" fill="#fff"/></svg><div style="font-size:6px;color:#fff;margin:5px 0 3px">Heading Here</div><div class="cell-text" style="text-align:left">Short note on this topic with a few words of detail for the team.</div></div>
  </div>
  <div class="foot"><span class="brand"><span class="dot"></span>Nexora</span><span class="copy">© Copyright Nexora. All rights reserved</span><span class="num">10</span></div>
</section>

<section class="slide" style="background:var(--blue)">
  <div class="abs brand" style="right:40px;top:112px;font-size:10px;color:var(--ink)"><span class="dot" style="width:8px;height:8px"></span>Nexora</div>
  <div class="abs" style="right:40px;top:130px;font-size:11px;font-weight:700;color:var(--ink)">Divider Page</div>
  <div class="abs" style="right:40px;top:145px;font-size:5px;color:var(--ink)">Subtitle Here</div>
  <div class="abs tiny" style="right:40px;top:154px;width:140px;text-align:right;color:#1f2f44">A short line to introduce the next section of this deck and set the scene.</div>
</section>

<section class="slide">
  <div class="s-title">Our Differences</div>
  <div class="abs" style="left:16px;top:50px;width:364px;height:118px;background:var(--blue)"></div>
  <div class="abs" style="left:30px;top:62px;width:180px">
    <div style="display:flex;gap:7px;align-items:center;margin-bottom:10px"><span class="ico" style="width:11px;height:11px;background:var(--ink)"><svg width="5" height="5"><circle cx="2.5" cy="2.5" r="2" fill="#fff"/></svg></span><span class="cell-text">We place proven tech talent in weeks,<br>not months, for every client.</span></div>
    <div style="display:flex;gap:7px;align-items:center;margin-bottom:10px"><span class="ico" style="width:11px;height:11px;background:var(--ink)"><svg width="5" height="5"><circle cx="2.5" cy="2.5" r="2" fill="#fff"/></svg></span><span class="cell-text">Deep sector focus across banking,<br>government and software.</span></div>
    <div style="display:flex;gap:7px;align-items:center;margin-bottom:10px"><span class="ico" style="width:11px;height:11px;background:var(--ink)"><svg width="5" height="5"><circle cx="2.5" cy="2.5" r="2" fill="#fff"/></svg></span><span class="cell-text">Consultants who understand the code<br>and the business behind it.</span></div>
    <div style="display:flex;gap:7px;align-items:center"><span class="ico" style="width:11px;height:11px;background:var(--ink)"><svg width="6" height="6"><circle cx="2.5" cy="2.5" r="2" stroke="#fff" fill="none"/><path d="M4 4L6 6" stroke="#fff"/></svg></span><span class="cell-text">Clear reporting and honest advice<br>from start to finish.</span></div>
  </div>
  <div class="photo ph-plane" role="img" aria-label="Photo of a laptop on a desk with a red paper plane" style="left:230px;top:62px;width:138px;height:90px"></div>
  <div class="foot"><span class="brand"><span class="dot"></span>Nexora</span><span class="copy">© Copyright Nexora. All rights reserved</span><span class="num">12</span></div>
</section>

<section class="slide">
  <div class="s-title">Text &amp; Bullet Area</div>
  <div class="abs" style="left:20px;top:40px;width:110px">
    <div style="font-size:6px;color:var(--blue);margin-bottom:6px">Heading Goes Here</div>
    <div class="tiny" style="margin-bottom:6px">A brief paragraph about this section goes here in a few short lines.</div>
    <div class="tiny" style="margin-bottom:6px">A second paragraph adds more detail about the work and results.</div>
    <div class="tiny">A closing line sums up the main idea for the reader.</div>
  </div>
  <div class="abs" style="left:148px;top:42px">
    <div style="display:flex;gap:6px;align-items:center;margin-bottom:13px"><span class="ico" style="width:12px;height:12px;background:var(--blue)"></span><div><div style="font-size:6px;color:var(--blue)">Your Text Here</div><div class="tiny">Short supporting line.</div></div></div>
    <div style="display:flex;gap:6px;align-items:center;margin-bottom:13px"><span class="ico" style="width:12px;height:12px;background:var(--ink)"></span><div><div style="font-size:6px;color:var(--ink)">Your Text Here</div><div class="tiny">Short supporting line.</div></div></div>
    <div style="display:flex;gap:6px;align-items:center;margin-bottom:13px"><span class="ico" style="width:12px;height:12px;background:var(--gray)"></span><div><div style="font-size:6px;color:var(--gray)">Your Text Here</div><div class="tiny">Short supporting line.</div></div></div>
    <div style="display:flex;gap:6px;align-items:center"><span class="ico" style="width:12px;height:12px;background:var(--blue)"></span><div><div style="font-size:6px;color:var(--blue)">Your Text Here</div><div class="tiny">Short supporting line.</div></div></div>
  </div>
  <div class="abs" style="left:268px;top:42px">
    <div style="display:flex;gap:6px;align-items:center;margin-bottom:13px"><span class="ico" style="width:12px;height:12px;background:#c9c9c9"></span><div><div style="font-size:6px;color:var(--gray-soft)">Your Text Here</div><div class="tiny">Short supporting line.</div></div></div>
    <div style="display:flex;gap:6px;align-items:center;margin-bottom:13px"><span class="ico" style="width:12px;height:12px;background:var(--gray)"></span><div><div style="font-size:6px;color:var(--gray)">Your Text Here</div><div class="tiny">Short supporting line.</div></div></div>
    <div style="display:flex;gap:6px;align-items:center;margin-bottom:13px"><span class="ico" style="width:12px;height:12px;background:var(--ink)"></span><div><div style="font-size:6px;color:var(--ink)">Your Text Here</div><div class="tiny">Short supporting line.</div></div></div>
    <div style="display:flex;gap:6px;align-items:center"><span class="ico" style="width:12px;height:12px;background:var(--blue)"></span><div><div style="font-size:6px;color:var(--blue)">Your Text Here</div><div class="tiny">Short supporting line.</div></div></div>
  </div>
  <div class="foot"><span class="brand"><span class="dot"></span>Nexora</span><span class="copy">© Copyright Nexora. All rights reserved</span><span class="num">13</span></div>
</section>

<section class="slide">
  <div class="abs" style="left:20px;top:22px;width:48px;height:24px;background:#2b2b2b"></div>
  <div class="abs" style="left:115px;top:18px;width:32px;height:32px;border-radius:50%;background:#2b2b2b"></div>
  <div class="abs" style="left:212px;top:20px;width:50px;height:28px;background:#2b2b2b;clip-path:polygon(0 0,100% 0,92% 100%,8% 100%)"></div>
  <div class="abs" style="left:310px;top:25px;width:52px;height:18px;border-radius:9px;background:#2b2b2b"></div>
  <div class="abs" style="left:20px;top:94px;width:44px;height:30px;border-radius:4px;background:#3a3a3a"></div>
  <div class="abs" style="left:98px;top:76px;width:200px;height:70px;background:var(--blue);display:flex;align-items:center;justify-content:center;text-align:center;color:#fff;font-size:15px;line-height:1.25">Our Awesome<br>Client</div>
  <div class="abs" style="left:318px;top:100px;width:50px;height:18px;border-radius:9px;border:2px solid #9a9a9a"></div>
  <div class="abs" style="left:22px;top:172px;width:32px;height:32px;border-radius:50%;border:3px solid #2b2b2b"></div>
  <div class="abs" style="left:116px;top:172px;width:32px;height:32px;border-radius:50%;background:#444"></div>
  <div class="abs" style="left:210px;top:174px;width:52px;height:28px;background:#2b2b2b;clip-path:polygon(50% 0,100% 60%,100% 100%,0 100%,0 60%)"></div>
  <div class="abs" style="left:314px;top:174px;width:50px;height:28px;background:#2b2b2b"></div>
</section>

<section class="slide" style="background:#000">
  <div class="abs brand white" style="right:34px;top:116px;font-size:10px"><span class="dot" style="width:8px;height:8px"></span>Nexora</div>
  <div class="abs" style="right:34px;top:134px;font-size:11px;font-weight:700;color:#fff">Divider Page</div>
  <div class="abs" style="right:34px;top:149px;font-size:5px;color:#fff">Subtitle Here</div>
  <div class="abs tiny light" style="right:34px;top:158px;width:150px;text-align:right">A short line to introduce the next section of this deck and set the scene.</div>
</section>

<section class="slide">
  <div class="abs" style="inset:0;display:grid;grid-template-columns:repeat(5,1fr)">
    <div style="background:var(--blue);padding:50px 7px 0"><div style="text-align:center"><svg width="18" height="18"><circle cx="9" cy="9" r="7" stroke="#fff" fill="none"/><circle cx="9" cy="9" r="2.5" fill="#fff"/></svg></div><div style="font-size:7px;color:#fff;margin:26px 0 4px">Heading Here</div><div class="cell-text">Short note on this column with a few lines of helpful detail.</div></div>
    <div style="background:var(--blue-mid);padding:50px 7px 0"><div style="text-align:center"><svg width="18" height="18"><rect x="2" y="3" width="14" height="10" stroke="#fff" fill="none"/><path d="M6 16H12" stroke="#fff"/></svg></div><div style="font-size:7px;color:#fff;margin:26px 0 4px">Heading Here</div><div class="cell-text">Short note on this column with a few lines of helpful detail.</div></div>
    <div style="background:var(--blue-soft);padding:50px 7px 0"><div style="text-align:center"><svg width="18" height="18"><circle cx="8" cy="8" r="5" stroke="#fff" fill="none"/><path d="M12 12L16 16" stroke="#fff"/></svg></div><div style="font-size:7px;color:#fff;margin:26px 0 4px">Heading Here</div><div class="cell-text">Short note on this column with a few lines of helpful detail.</div></div>
    <div style="background:#5b84b0;padding:50px 7px 0"><div style="text-align:center"><svg width="18" height="18"><rect x="2" y="2" width="14" height="14" stroke="#fff" fill="none"/><circle cx="9" cy="9" r="3" stroke="#fff" fill="none"/></svg></div><div style="font-size:7px;color:#fff;margin:26px 0 4px">Heading Here</div><div class="cell-text">Short note on this column with a few lines of helpful detail.</div></div>
    <div style="background:#0d0d0d;padding:50px 7px 0"><div style="text-align:center"><svg width="18" height="18"><circle cx="9" cy="9" r="7.5" stroke="#fff" fill="none"/><circle cx="9" cy="9" r="4" stroke="#fff" fill="none"/></svg></div><div style="font-size:7px;color:#fff;margin:26px 0 4px">Heading Here</div><div class="cell-text">Short note on this column with a few lines of helpful detail.</div></div>
  </div>
</section>

<section class="slide">
  <div class="s-title">Our Mockup Area</div>
  <div class="abs brand" style="right:14px;top:12px;font-size:8px"><span class="dot" style="width:6px;height:6px;border-width:1.5px"></span>Nexora</div>
  <div class="abs" style="left:0;top:120px;width:396px;height:103px;background:var(--blue)"></div>
  <div class="abs" style="left:85px;top:38px;width:226px;height:145px;background:#1d1d1d;border-radius:6px 6px 0 0;padding:7px"><div style="width:100%;height:100%;background:#fff;display:flex;align-items:center;justify-content:center"><span class="brand" style="font-size:24px"><span class="dot" style="width:16px;height:16px;border-width:3px"></span>Nexora</span></div></div>
  <div class="abs" style="left:68px;top:183px;width:260px;height:6px;background:#cfcfcf;border-radius:0 0 8px 8px"></div>
  <svg class="abs" style="left:0;top:0" width="396" height="223"><g stroke="#333" stroke-width=".7" fill="none"><path d="M58 66H150"/><path d="M58 96H120"/><path d="M58 130H110"/><path d="M338 66H250"/><path d="M338 92H285"/><path d="M338 130H300"/></g><circle cx="150" cy="66" r="1.8" fill="#4c78a8"/><circle cx="250" cy="66" r="1.8" fill="#4c78a8"/></svg>
  <div class="abs" style="left:14px;top:60px;width:44px;height:12px;background:var(--blue);color:#fff;font-size:4.5px;padding:2px 3px">Your Text<br>Goes Here</div>
  <div class="abs" style="left:14px;top:90px;width:44px;height:12px;background:var(--ink);color:#fff;font-size:4.5px;padding:2px 3px">Your Text<br>Goes Here</div>
  <div class="abs" style="left:14px;top:124px;width:44px;height:12px;background:var(--gray);color:#fff;font-size:4.5px;padding:2px 3px">Your Text<br>Goes Here</div>
  <div class="abs" style="left:338px;top:60px;width:44px;height:12px;background:var(--gray);color:#fff;font-size:4.5px;padding:2px 3px">Your Text<br>Goes Here</div>
  <div class="abs" style="left:338px;top:86px;width:44px;height:12px;background:var(--blue-soft);color:#fff;font-size:4.5px;padding:2px 3px">Your Text<br>Goes Here</div>
  <div class="abs" style="left:338px;top:124px;width:44px;height:12px;background:var(--ink);color:#fff;font-size:4.5px;padding:2px 3px">Your Text<br>Goes Here</div>
</section>

<section class="slide">
  <div class="abs" style="left:0;top:0;width:196px;height:223px;background:var(--blue)"></div>
  <div class="abs" style="left:58px;top:34px;width:80px;height:80px;border-radius:50%;border:1.5px solid #fff;display:flex;align-items:center;justify-content:center;text-align:center;color:#fff;font-size:9px;line-height:1.2">RIGHT<br>PICTURE<br>SLIDE</div>
  <div class="abs tiny light" style="left:32px;top:148px;width:132px;text-align:center">A short paragraph explains the chart on the right and the growth it shows over the past year.</div>
  <svg class="abs" style="left:218px;top:18px" width="165" height="115" viewBox="0 0 165 115"><g><rect x="6" y="40" width="8" height="70" fill="#4c78a8"/><rect x="16" y="30" width="8" height="80" fill="#111"/><rect x="36" y="52" width="8" height="58" fill="#4c78a8"/><rect x="46" y="22" width="8" height="88" fill="#111"/><rect x="66" y="48" width="8" height="62" fill="#4c78a8"/><rect x="76" y="36" width="8" height="74" fill="#111"/><rect x="96" y="44" width="8" height="66" fill="#4c78a8"/><rect x="106" y="26" width="8" height="84" fill="#111"/><rect x="126" y="30" width="8" height="80" fill="#4c78a8"/><rect x="136" y="8" width="8" height="102" fill="#111"/></g><path d="M0 110H160" stroke="#ccc" stroke-width=".6"/></svg>
  <svg class="abs" style="left:222px;top:152px" width="12" height="11"><path d="M6 0L12 11H0Z" fill="#4c78a8"/></svg>
  <div class="abs" style="left:238px;top:143px;font-size:20px;color:#444">85%</div>
  <div class="abs" style="left:238px;top:167px;font-size:5.5px;font-weight:700;color:#333">Profit</div>
  <div class="abs tiny" style="left:238px;top:175px;width:120px">Yearly profit rose on strong demand for our services.</div>
</section>

<section class="slide">
  <div class="abs" style="left:0;top:0;width:396px;height:132px;background:var(--blue)"></div>
  <div class="abs" style="left:14px;top:12px;font-size:10px;color:#fff">Our Mockup Area</div>
  <div class="abs" style="left:14px;top:42px;font-size:6.5px;color:#fff">Heading Here</div>
  <div class="abs tiny light" style="left:14px;top:52px;width:150px">A short paragraph describes how our platform looks on a desktop screen and what clients can do with it each day.</div>
  <div class="abs" style="left:178px;top:20px;width:190px;height:120px;background:#1a1a1a;border-radius:4px;padding:6px"><div style="width:100%;height:100%;background:#fff;display:flex;align-items:center;justify-content:center"><span class="brand" style="font-size:24px"><span class="dot" style="width:16px;height:16px;border-width:3px"></span>Nexora</span></div></div>
  <div class="abs" style="left:258px;top:140px;width:30px;height:22px;background:#c8c8c8"></div>
  <div class="abs" style="left:240px;top:162px;width:66px;height:4px;background:#b3b3b3;border-radius:2px"></div>
  <div class="abs" style="left:14px;top:140px;display:flex;gap:6px;align-items:center"><span class="ico" style="width:10px;height:10px;background:var(--blue)"></span><span class="tiny" style="width:130px">A short note about the first key feature of the product.</span></div>
  <div class="abs" style="left:14px;top:166px;display:flex;gap:6px;align-items:center"><span class="ico" style="width:10px;height:10px;background:var(--ink)"></span><span class="tiny" style="width:130px">A short note about the second key feature of the product.</span></div>
  <div class="foot"><span class="brand"><span class="dot"></span>Nexora</span><span class="copy">© Copyright Nexora. All rights reserved</span><span class="num">19</span></div>
</section>

<section class="slide">
  <div class="abs" style="left:20px;top:40px;font-size:12px;color:#444;line-height:1.25">This Is Line<br>Chart Slide</div>
  <div class="abs" style="left:20px;top:80px;width:88px;height:13px;background:var(--blue);color:#fff;font-size:5.5px;display:flex;align-items:center;justify-content:center">Creative Text Here</div>
  <div class="abs tiny" style="left:20px;top:102px;width:110px">A short paragraph explains the two trends in this chart and what they mean for our clients this year.</div>
  <svg class="abs" style="left:180px;top:20px" width="205" height="165" viewBox="0 0 205 165">
    <g stroke="#eee" stroke-width=".6"><path d="M12 10H200M12 35H200M12 60H200M12 85H200M12 110H200M12 135H200"/></g>
    <g font-size="4" fill="#999" font-family="Raleway, sans-serif"><text x="2" y="12">6</text><text x="2" y="37">5</text><text x="2" y="62">4</text><text x="2" y="87">3</text><text x="2" y="112">2</text><text x="2" y="137">1</text><text x="22" y="148">Category 1</text><text x="72" y="148">Category 2</text><text x="122" y="148">Category 3</text><text x="172" y="148">Category 4</text></g>
    <polyline points="30,40 80,82 130,50 180,15" fill="none" stroke="#111" stroke-width="1.2"/>
    <polyline points="30,78 80,30 130,98 180,72" fill="none" stroke="#4c78a8" stroke-width="1.2"/>
    <g fill="#111"><circle cx="30" cy="40" r="1.8"/><circle cx="80" cy="82" r="1.8"/><circle cx="130" cy="50" r="1.8"/><circle cx="180" cy="15" r="1.8"/></g>
  </svg>
  <div class="foot"><span class="brand"><span class="dot"></span>Nexora</span><span class="copy">© Copyright Nexora. All rights reserved</span><span class="num">20</span></div>
</section>

<section class="slide">
  <div class="s-title">Your Title Goes Here</div>
  <div class="abs" style="left:31px;top:43px;width:338px;height:142px;display:grid;grid-template-columns:repeat(3,1fr);grid-template-rows:repeat(2,1fr)">
    <div class="ph-office-a" role="img" aria-label="Photo of colleagues working at computers"></div>
    <div style="background:var(--ink);padding:8px"><div style="font-size:7px;color:#fff;margin-bottom:3px">Heading Goes Here</div><div class="cell-text">Short note on this idea in a couple of lines.</div></div>
    <div class="ph-office-b" role="img" aria-label="Photo of a person at a laptop"></div>
    <div style="background:var(--blue);padding:8px"><div style="font-size:7px;color:#fff;margin-bottom:3px">Heading Goes Here</div><div class="cell-text">Short note on this idea in a couple of lines.</div></div>
    <div class="ph-office-c" role="img" aria-label="Photo of a team at a desk"></div>
    <div style="background:var(--gray);padding:8px"><div style="font-size:7px;color:#fff;margin-bottom:3px">Heading Goes Here</div><div class="cell-text">Short note on this idea in a couple of lines.</div></div>
  </div>
  <div class="foot"><span class="brand"><span class="dot"></span>Nexora</span><span class="copy">© Copyright Nexora. All rights reserved</span><span class="num">21</span></div>
</section>

<section class="slide">
  <div class="photo ph-about" role="img" aria-label="Warm toned photo of a laptop showing a web page" style="left:0;top:0;width:280px;height:223px"></div>
  <div class="abs" style="left:200px;top:72px;width:196px;height:100px;background:var(--blue);padding:10px 12px">
    <div style="font-size:10px;color:#fff;margin-bottom:5px">About Us</div>
    <div class="cell-text">We are a Canadian technology consulting and recruiting firm that helps teams find the right people.</div>
    <div class="cell-text" style="margin-top:5px">Our consultants bring deep sector knowledge to each search.</div>
  </div>
</section>

<section class="slide">
  <div class="photo ph-suit" role="img" aria-label="Blue toned photo of a businessman in a suit" style="inset:0"></div>
  <div class="abs brand white" style="right:20px;top:14px;font-size:13px"><span class="dot" style="width:9px;height:9px"></span>Nexora</div>
  <div class="abs h-big" style="left:26px;top:150px;font-size:15px">This Is Your Divider Page</div>
  <div class="abs sub" style="left:26px;top:171px">Your Subtitle Goes Here</div>
</section>

<section class="slide">
  <div class="s-title">Quote Area</div>
  <div class="abs" style="left:0;top:48px;width:396px;height:112px;background:var(--blue)"></div>
  <div class="photo ph-towers" role="img" aria-label="Photo of a businessman walking past glass office towers" style="left:196px;top:48px;width:200px;height:112px"></div>
  <div class="abs" style="left:20px;top:72px;width:170px;color:#fff;font-size:7.5px;line-height:1.35">“Coming together is a beginning. Keeping together is progress. Working together is success.”</div>
  <div class="abs" style="left:34px;top:122px;color:#fff;font-size:7px">Walter Brenn</div>
  <div class="foot"><span class="brand"><span class="dot"></span>Nexora</span><span class="copy">© Copyright Nexora. All rights reserved</span><span class="num">24</span></div>
</section>

<section class="slide">
  <div class="s-title">Brand Detailed</div>
  <div class="photo ph-brand" role="img" aria-label="Photo of a laptop with a hand on the keyboard" style="left:14px;top:48px;width:180px;height:110px"></div>
  <div class="abs" style="left:204px;top:38px;width:180px;height:150px;display:grid;grid-template-columns:1fr 1fr;grid-template-rows:1fr 1fr;gap:4px">
    <div style="background:var(--blue);padding:7px;text-align:center"><div style="font-size:6px;color:#fff;margin-bottom:3px">System</div><div class="cell-text">Short note on our<br>reliable systems.</div></div>
    <div style="background:var(--ink);padding:7px;text-align:center"><div style="font-size:6px;color:#fff;margin-bottom:3px">Technology</div><div class="cell-text">Short note on our<br>modern tools.</div></div>
    <div style="background:var(--gray);padding:7px;text-align:center"><div style="font-size:6px;color:#fff;margin-bottom:3px">Leisure</div><div class="cell-text">Short note on our<br>team culture.</div></div>
    <div style="background:var(--gray-soft);padding:7px;text-align:center"><div style="font-size:6px;color:#fff;margin-bottom:3px">Digital</div><div class="cell-text">Short note on our<br>digital work.</div></div>
  </div>
  <div class="foot"><span class="brand"><span class="dot"></span>Nexora</span><span class="copy">© Copyright Nexora. All rights reserved</span><span class="num">25</span></div>
</section>

<section class="slide">
  <div class="s-title">Product Philosophy</div>
  <svg class="abs" style="left:148px;top:60px" width="100" height="100" viewBox="0 0 100 100">
    <g transform="rotate(-90 50 50)" fill="none" stroke-width="20">
      <circle cx="50" cy="50" r="30" stroke="#4c78a8" stroke-dasharray="75.4 188.5" stroke-dashoffset="0"/>
      <circle cx="50" cy="50" r="30" stroke="#111" stroke-dasharray="28.3 188.5" stroke-dashoffset="-75.4"/>
      <circle cx="50" cy="50" r="30" stroke="#6f6f6f" stroke-dasharray="47.1 188.5" stroke-dashoffset="-103.7"/>
      <circle cx="50" cy="50" r="30" stroke="#b5b5b5" stroke-dasharray="37.7 188.5" stroke-dashoffset="-150.8"/>
    </g>
    <g font-size="5.5" fill="#fff" font-family="Raleway, sans-serif" text-anchor="middle"><text x="60" y="28">15%</text><text x="78" y="56">25%</text><text x="48" y="82">20%</text><text x="24" y="50">40%</text></g>
  </svg>
  <div class="abs" style="left:30px;top:44px;display:flex;gap:6px;align-items:center"><div style="text-align:right;width:58px"><div style="font-size:5.5px;color:var(--blue)">Mission</div><div class="tiny">Short line about<br>our mission here.</div></div><span class="ico" style="width:18px;height:18px;background:var(--blue)"><svg width="8" height="8"><circle cx="4" cy="4" r="3" stroke="#fff" fill="none"/></svg></span></div>
  <div class="abs" style="left:30px;top:118px;display:flex;gap:6px;align-items:center"><div style="text-align:right;width:58px"><div style="font-size:5.5px;color:var(--gray-soft)">Vision</div><div class="tiny">Short line about<br>our vision here.</div></div><span class="ico" style="width:18px;height:18px;background:#c4c4c4"><svg width="8" height="8"><circle cx="4" cy="3" r="2.5" fill="#fff"/></svg></span></div>
  <div class="abs" style="left:268px;top:44px;display:flex;gap:6px;align-items:center"><span class="ico" style="width:18px;height:18px;background:var(--ink)"><svg width="8" height="8"><path d="M1 7L7 1" stroke="#fff"/></svg></span><div style="width:70px"><div style="font-size:5.5px;color:var(--ink)">Strategy</div><div class="tiny">Short line about<br>our strategy here.</div></div></div>
  <div class="abs" style="left:268px;top:118px;display:flex;gap:6px;align-items:center"><span class="ico" style="width:18px;height:18px;background:var(--gray)"><svg width="8" height="8"><rect x="1" y="2" width="6" height="4" stroke="#fff" fill="none"/></svg></span><div style="width:70px"><div style="font-size:5.5px;color:var(--gray)">Execution</div><div class="tiny">Short line about<br>our delivery here.</div></div></div>
  <div class="foot"><span class="brand"><span class="dot"></span>Nexora</span><span class="copy">© Copyright Nexora. All rights reserved</span><span class="num">26</span></div>
</section>

<section class="slide">
  <div class="photo ph-city" role="img" aria-label="Faded photo of a city skyline" style="inset:0"></div>
  <svg class="abs" style="left:0;top:0" width="396" height="223" viewBox="0 0 396 223">
    <g font-family="Raleway, sans-serif" font-size="5" fill="#333" text-anchor="middle">
      <rect x="28" y="95" width="20" height="60" fill="#4c78a8"/><rect x="52" y="80" width="20" height="75" fill="#111"/><text x="38" y="91">400</text><text x="62" y="76">500</text>
      <rect x="112" y="110" width="20" height="45" fill="#4c78a8"/><rect x="136" y="65" width="20" height="90" fill="#111"/><text x="122" y="106">300</text><text x="146" y="61">600</text>
      <rect x="196" y="125" width="20" height="30" fill="#4c78a8"/><rect x="220" y="125" width="20" height="30" fill="#111"/><text x="206" y="121">200</text><text x="230" y="121">200</text>
      <rect x="280" y="125" width="20" height="30" fill="#4c78a8"/><rect x="304" y="140" width="20" height="15" fill="#111"/><text x="290" y="121">200</text><text x="314" y="136">100</text>
      <g font-weight="700" font-size="5.5"><text x="50" y="168">Asia</text><text x="134" y="168">Africa</text><text x="218" y="168">America</text><text x="302" y="168">Euro</text></g>
      <g fill="#888" font-size="4.3"><text x="50" y="176">Steady growth in</text><text x="50" y="182">placements.</text><text x="134" y="176">Strong demand for</text><text x="134" y="182">new talent.</text><text x="218" y="176">Stable results</text><text x="218" y="182">across teams.</text><text x="302" y="176">Early stage</text><text x="302" y="182">expansion.</text></g>
    </g>
  </svg>
</section>

<section class="slide">
  <div class="s-title">Trending In The World</div>
  <div class="photo ph-map" role="img" aria-label="World map silhouette in light gray" style="left:8px;top:34px;width:252px;height:150px"></div>
  <div class="abs ico" style="left:40px;top:96px;width:26px;height:26px;background:#9a9a9a;color:#fff;font-size:7px">25%</div>
  <div class="abs ico" style="left:105px;top:80px;width:38px;height:38px;background:#2a2a2a;color:#fff;font-size:10px">80%</div>
  <div class="abs ico" style="left:215px;top:90px;width:32px;height:32px;background:#8f8f8f;color:#fff;font-size:9px">75%</div>
  <div class="abs ico" style="left:178px;top:140px;width:24px;height:24px;background:#b0b0b0;color:#fff;font-size:6.5px">35%</div>
  <div class="abs" style="left:275px;top:56px">
    <div style="display:flex;gap:6px;align-items:center;margin-bottom:14px"><span class="ico" style="width:16px;height:16px;border:1px solid #999"><svg width="8" height="8"><rect x="1" y="1" width="6" height="6" stroke="#666" fill="none"/></svg></span><div><div style="font-size:5.5px;color:var(--gray)">Consistent</div><div class="tiny">Short line of detail<br>on this trend.</div></div></div>
    <div style="display:flex;gap:6px;align-items:center;margin-bottom:14px"><span class="ico" style="width:16px;height:16px;border:1px solid #999"><svg width="8" height="8"><circle cx="4" cy="4" r="3" stroke="#666" fill="none"/></svg></span><div><div style="font-size:5.5px;color:var(--gray)">Intangible</div><div class="tiny">Short line of detail<br>on this trend.</div></div></div>
    <div style="display:flex;gap:6px;align-items:center"><span class="ico" style="width:16px;height:16px;border:1px solid #999"><svg width="8" height="8"><path d="M1 7V4M4 7V2M7 7V5" stroke="#666"/></svg></span><div><div style="font-size:5.5px;color:var(--gray)">Performance</div><div class="tiny">Short line of detail<br>on this trend.</div></div></div>
  </div>
  <div class="foot"><span class="brand"><span class="dot"></span>Nexora</span><span class="copy">© Copyright Nexora. All rights reserved</span><span class="num">28</span></div>
</section>

<section class="slide">
  <div class="s-title">Our Vision &amp; Mission</div>
  <div class="photo ph-building" role="img" aria-label="Blue toned photo of a modern building" style="left:0;top:32px;width:396px;height:172px"></div>
  <div class="abs" style="left:18px;top:44px;width:170px;color:#fff">
    <div style="font-size:8px;margin-bottom:4px">• Our Vision:</div>
    <div style="font-size:7px;font-weight:700;line-height:1.3;margin-bottom:6px">Go to the Next Level<br>Without look in the past</div>
    <div class="cell-text">We aim to be the trusted partner for tech hiring across Canada, linking great people with great teams every day.</div>
  </div>
  <div class="abs" style="left:205px;top:44px;width:175px;color:#fff">
    <div style="font-size:8px;margin-bottom:6px">• Our Missions:</div>
    <div style="display:flex;gap:6px;margin-bottom:8px"><span class="ico" style="width:10px;height:10px;background:#fff"></span><div><div style="font-size:6.5px">Your Text Here</div><div class="cell-text">Short line about this mission.</div></div></div>
    <div style="display:flex;gap:6px;margin-bottom:8px"><span class="ico" style="width:10px;height:10px;background:#fff"></span><div><div style="font-size:6.5px">Your Text Here</div><div class="cell-text">Short line about this mission.</div></div></div>
    <div style="display:flex;gap:6px"><span class="ico" style="width:10px;height:10px;background:#fff"></span><div><div style="font-size:6.5px">Your Text Here</div><div class="cell-text">Short line about this mission.</div></div></div>
  </div>
  <div class="foot"><span class="brand"><span class="dot"></span>Nexora</span><span class="copy">© Copyright Nexora. All rights reserved</span><span class="num">29</span></div>
</section>

<section class="slide">
  <div class="s-title">Our Services</div>
  <div class="photo ph-service" role="img" aria-label="Photo of a businessman working on a laptop" style="left:14px;top:36px;width:180px;height:110px"></div>
  <div class="abs" style="left:14px;top:154px;font-size:7px;color:var(--blue)">Your Title Goes Here</div>
  <div class="abs tiny" style="left:14px;top:164px;width:175px">A short paragraph about the services we offer to banks, government and tech firms.</div>
  <div class="abs" style="left:212px;top:40px;width:170px">
    <div style="display:flex;gap:7px;margin-bottom:16px"><span class="ico" style="width:14px;height:14px;background:var(--blue);flex:none"><svg width="7" height="7"><path d="M1 6V3M3.5 6V1M6 6V4" stroke="#fff"/></svg></span><div><div style="font-size:6.5px;color:var(--blue)">Service Number One</div><div class="tiny">Short line about this service and<br>the value it brings to clients.</div></div></div>
    <div style="display:flex;gap:7px;margin-bottom:16px"><span class="ico" style="width:14px;height:14px;background:var(--ink);flex:none"><svg width="7" height="7"><path d="M1 6L6 1M3 1H6V4" stroke="#fff" fill="none"/></svg></span><div><div style="font-size:6.5px;color:var(--ink)">Service Number Two</div><div class="tiny">Short line about this service and<br>the value it brings to clients.</div></div></div>
    <div style="display:flex;gap:7px"><span class="ico" style="width:14px;height:14px;background:var(--gray);flex:none"><svg width="7" height="7"><circle cx="3" cy="3" r="2" stroke="#fff" fill="none"/><path d="M4.5 4.5L6.5 6.5" stroke="#fff"/></svg></span><div><div style="font-size:6.5px;color:var(--gray)">Service Number Three</div><div class="tiny">Short line about this service and<br>the value it brings to clients.</div></div></div>
  </div>
  <div class="foot"><span class="brand"><span class="dot"></span>Nexora</span><span class="copy">© Copyright Nexora. All rights reserved</span><span class="num">30</span></div>
</section>

</main>
</body>
</html>
```